Commercial Real Estate

We need a business card design for a new commercial real estate business that specializes in apartment building brokerage. Not individual units but the entire complex. We find and represent the owners existing buildings and well as new buyers for those buildings. The design should convey trust, integrity, knowledge and growth. It should be easily read.

Target Market(s)

40 to 65 years old

Industry/Entity Type

Real Estate

```html
<!DOCTYPE html>
<html lang="en">
<head>
<meta charset="utf-8">
<title>Keystead Property Investments – Business Card</title>
<link href="https://fonts.googleapis.com/css2?family=Inter:wght@300;400;600;700&display=swap" rel="stylesheet">
<style>
  :root {
    --slate: #4b5b5c;
    --teal: #6cc6c4;
    --card-light: #ececec;
    --ink: #4f5556;
    --white: #ffffff;
    --backdrop: #d9dbdc;
  }
  * { margin: 0; padding: 0; box-sizing: border-box; }
  html, body {
    width: 1200px; height: 900px; overflow: hidden;
    background: var(--backdrop);
    font-family: "Inter", Helvetica, Arial, sans-serif;
  }
  .stage {
    width: 1200px; height: 900px;
    display: flex; align-items: center; justify-content: center; gap: 90px;
  }
  .card {
    width: 360px; height: 630px; position: relative; overflow: hidden;
    box-shadow: 0 6px 20px rgba(0,0,0,0.18);
  }

  /* Front */
  .card-front { background: var(--slate); color: var(--white); }
  .front-brand {
    position: absolute; top: 230px; left: 0; right: 0;
    display: flex; flex-direction: column; align-items: center;
  }
  .brand-row { display: flex; align-items: center; gap: 12px; }
  .brand-square { width: 18px; height: 18px; background: var(--teal); }
  .brand-name {
    font-weight: 700; font-size: 40px; letter-spacing: 3px; color: var(--white);
  }
  .brand-rule { width: 220px; height: 2px; background: var(--teal); margin: 14px 0 10px; }
  .brand-tagline {
    font-weight: 600; font-size: 14px; letter-spacing: 2.5px; color: var(--white);
  }
  .front-web {
    position: absolute; bottom: 70px; left: 0; right: 0; text-align: center;
    color: var(--teal); font-size: 17px; font-weight: 400; letter-spacing: 0.5px;
  }

  /* Back */
  .card-back { background: var(--card-light); color: var(--ink); }
  .back-brand {
    height: 200px; display: flex; align-items: center; padding-left: 40px; gap: 12px;
  }
  .back-brand .brand-square { background: var(--slate); }
  .back-brand .brand-name { color: var(--slate); font-size: 30px; }
  .name-band {
    background: var(--slate); color: var(--white);
    padding: 22px 40px 18px; border-bottom: 3px solid var(--teal);
  }
  .person-name { font-weight: 300; font-size: 28px; }
  .person-role { font-weight: 300; font-size: 17px; margin-top: 4px; }
  .contact-list { list-style: none; padding: 34px 40px 0; font-size: 17px; font-weight: 300; line-height: 1.35; }
  .contact-key { display: inline-block; width: 22px; color: var(--teal); font-weight: 700; }
  .postal { padding: 26px 40px 0; font-size: 17px; font-weight: 300; line-height: 1.35; }
  .back-web { padding: 30px 40px 0; font-size: 20px; font-weight: 700; color: var(--ink); }
</style>
</head>
<body>
<main class="stage">
  <section class="card card-front">
    <div class="front-brand">
      <div class="brand-row">
        <span class="brand-square"></span>
        <span class="brand-name">KEYSTEAD</span>
      </div>
      <div class="brand-rule"></div>
      <div class="brand-tagline">Property Investments</div>
    </div>
    <div class="front-web">www.keystead.com</div>
  </section>

  <section class="card card-back">
    <div class="back-brand">
      <span class="brand-square"></span>
      <span class="brand-name">KEYSTEAD</span>
    </div>
    <div class="name-band">
      <div class="person-name">Tomas Reyland</div>
      <div class="person-role">Manager</div>
    </div>
    <ul class="contact-list">
      <li><span class="contact-key">T</span>0400 555 218</li>
      <li><span class="contact-key">F</span>0400 555 219</li>
      <li><span class="contact-key">E</span>tomas.reyland@keystead.com</li>
    </ul>
    <p class="postal">PO Box 2214 Marlow<br>Creek NT 0870</p>
    <p class="back-web">www.keystead.com</p>
  </section>
</main>
</body>
</html>
```